Packaging Tape Design for Retail / Ecommerce Company

We need a design for custom packing tape for our company. We would like to see two designs for the packaging tape. 1) with the word fragile attached 2) Similiar design without the fragileMinimum resolution is 300 .ppi 3" x 6" or 3" x 12" - If selected, request that font that are used be identified. ZOR Havenly Logo and package - Nest Bright! is a tagline we use on documents and correspondence. Looking for a creative design.

Target Market(s)

Mid level to high end consumers

Industry/Entity Type

Retail

Font styles to use
Sans Serif

Requirements
Must have
• logo must be included
• Nest Bright! - must be included
• web address: zorhavenly.example
Nice to have
• creativity

```html
<!DOCTYPE html>
<html lang="en">
<head>
<meta charset="utf-8">
<title>ZOR Havenly – Fragile Packing Tape</title>
<link rel="stylesheet" href="https://fonts.googleapis.com/css2?family=Chakra+Petch:wght@700&display=swap">
<style>
  :root {
    --tape-maroon: #6b2220;
    --tape-white: #ffffff;
  }
  html, body {
    margin: 0;
    padding: 0;
    width: 1200px;
    height: 300px;
    overflow: hidden;
    background: var(--tape-white);
  }
  .tape {
    position: relative;
    width: 1200px;
    height: 300px;
    background: var(--tape-white);
    overflow: hidden;
    font-family: "Chakra Petch", sans-serif;
    font-weight: 700;
    color: var(--tape-white);
  }
  .stripe {
    position: absolute;
    left: 0;
    width: 100%;
    background: var(--tape-maroon);
  }
  .stripe--top-outer { top: 3px; height: 7px; }
  .stripe--top-inner { top: 22px; height: 7px; }
  .stripe--bottom-inner { top: 273px; height: 6px; }
  .stripe--bottom-outer { top: 290px; height: 7px; }
  .band {
    position: absolute;
    left: 0;
    top: 37px;
    width: 100%;
    height: 227px;
    background: var(--tape-maroon);
  }
  .warning {
    position: absolute;
    left: 66px;
    top: 48px;
    margin: 0;
    font-size: 184px;
    font-weight: 700;
    line-height: 184px;
    letter-spacing: 0;
    white-space: nowrap;
  }
  .brand {
    position: absolute;
    left: 905px;
    top: 62px;
    width: 245px;
    text-align: center;
    white-space: nowrap;
  }
  .brand__name {
    height: 116px;
    line-height: 116px;
    font-size: 30px;
    letter-spacing: 1px;
  }
  .brand__tagline {
    margin-top: 26px;
    font-size: 27px;
    line-height: 30px;
    letter-spacing: 1px;
  }
  .brand__web {
    margin-top: 6px;
    font-size: 15px;
    line-height: 18px;
    letter-spacing: 0.5px;
  }
</style>
</head>
<body>
  <div class="tape">
    <div class="stripe stripe--top-outer"></div>
    <div class="stripe stripe--top-inner"></div>
    <div class="band"></div>
    <h1 class="warning">FRAGILE</h1>
    <div class="brand">
      <div class="brand__name">ZOR HAVENLY</div>
      <div class="brand__tagline">NEST BRIGHT!</div>
      <div class="brand__web">zorhavenly.example</div>
    </div>
    <div class="stripe stripe--bottom-inner"></div>
    <div class="stripe stripe--bottom-outer"></div>
  </div>
</body>
</html>
```